Bamboo Toothbrush packaging design

We need a packaging design for a pack of 4 bamboo toothbrushes. The front of the package would need to include the company logo, name of the product - Bamboo Toothbrush, 100% plastic free, and 10% of profit will go to environmental charities . Would like to see some simple or creative graphics to send the message.

Target Market(s)

Retail

Font styles to use
Sans Serif

Colors

Designer to choose colors to be used in the design.

Requirements
Must have
• Just be creative.

```html
<!DOCTYPE html>
<html lang="en">
<head>
<meta charset="utf-8">
<title>Swift Heron – Bamboo Toothbrush Box Dieline</title>
<link rel="stylesheet" href="https://fonts.googleapis.com/css2?family=Roboto:wght@400;500&family=Roboto+Condensed:wght@400;500&display=swap">
<style>
  :root {
    --navy: #1c3340;
    --paper: #ffffff;
    --cut-line: #6b6b6b;
    --bamboo-ink: #1c3340;
    --page-bg: #ffffff;
  }
  html, body {
    margin: 0;
    padding: 0;
    width: 1200px;
    height: 1000px;
    overflow: hidden;
    background: var(--page-bg);
  }
  .dieline {
    display: block;
    width: 1200px;
    height: 1000px;
  }
  .panel-dark { fill: var(--navy); }
  .panel-light { fill: var(--paper); stroke: var(--cut-line); stroke-width: 0.8; }
  .fold-line { stroke: var(--cut-line); stroke-width: 0.6; fill: none; }
  .fold-line-light { stroke: #4a5f6b; stroke-width: 0.6; fill: none; }
  .badge { fill: var(--paper); }
  .badge-mark { fill: var(--navy); }
  .badge-text {
    font-family: "Roboto Condensed", sans-serif;
    font-weight: 500;
    fill: var(--navy);
  }
  .brand-name {
    font-family: "Roboto", sans-serif;
    font-weight: 400;
    fill: var(--paper);
  }
  .brand-name--flap { fill: var(--navy); }
  .profit-title {
    font-family: "Roboto Condensed", sans-serif;
    font-weight: 500;
    font-size: 19px;
    fill: var(--navy);
  }
  .profit-note {
    font-family: "Roboto Condensed", sans-serif;
    font-weight: 500;
    font-size: 7.4px;
    fill: var(--navy);
  }
  .claim {
    font-family: "Roboto", sans-serif;
    font-weight: 400;
    font-size: 19px;
    fill: var(--navy);
  }
  .product-name {
    font-family: "Roboto Condensed", sans-serif;
    font-weight: 500;
    font-size: 33px;
    letter-spacing: 0.3px;
    fill: var(--navy);
  }
  .bamboo-art { fill: var(--bamboo-ink); }
</style>
</head>
<body>
<svg class="dieline" viewBox="0 0 1200 1000" xmlns="http://www.w3.org/2000/svg">
  <defs>
    <linearGradient id="bamboo-tone" x1="0" y1="0" x2="1" y2="0">
      <stop offset="0" stop-color="#1c3340" stop-opacity="0.55"/>
      <stop offset="0.5" stop-color="#1c3340"/>
      <stop offset="1" stop-color="#1c3340" stop-opacity="0.55"/>
    </linearGradient>

    <g id="badge-row">
      <rect class="badge" x="218" y="555" width="60" height="33" rx="4"/>
      <rect class="badge-mark" x="224" y="561" width="8" height="21" rx="1" role="img" aria-label="Small bamboo stalk icon"/>
      <text class="badge-text" x="236" y="574.5" font-size="6.5">BAMBOO</text>

      <rect class="badge" x="308" y="555" width="60" height="33" rx="4"/>
      <rect class="badge-mark" x="311" y="558" width="54" height="14" rx="2"/>
      <text class="badge-text" x="338" y="569" font-size="10.5" text-anchor="middle" fill="#ffffff" style="fill:#ffffff">ECO</text>
      <text class="badge-text" x="338" y="583" font-size="9" text-anchor="middle" font-weight="400">FRIENDLY</text>

      <rect class="badge" x="397" y="555" width="61" height="33" rx="4"/>
      <rect class="badge-mark" x="403" y="563" width="16" height="16" rx="3" role="img" aria-label="Recycling symbol"/>
      <text class="badge-text" x="423" y="574.5" font-size="6.5">RECYCLE</text>
    </g>

    <g id="claim-row">
      <text class="profit-title" x="533" y="580">10% OF PROFIT</text>
      <text class="profit-note" x="533" y="589">GO TO ENVIRONMENTAL CHARITIES</text>
      <rect x="682" y="552" width="18" height="42" fill="url(#bamboo-tone)" role="img" aria-label="Small bamboo sprig"/>
      <text class="claim" x="727" y="580">100% natural bamboo toothbrush</text>
    </g>
  </defs>

  <g transform="translate(0,-247)">
    <!-- Row 1: top side panel -->
    <rect class="panel-dark" x="135" y="537" width="360" height="70"/>
    <line class="fold-line-light" x1="180" y1="537" x2="180" y2="607"/>
    <rect class="panel-light" x="495" y="537" width="527" height="70"/>
    <path class="panel-light" d="M1022 539 L1067 539 L1067 583 L1060 605 L1022 605 Z"/>
    <use href="#badge-row"/>
    <use href="#claim-row"/>

    <!-- Row 2: front panel with left tuck flap -->
    <path class="panel-dark" d="M180 607 L180 719 L56 719 Q42 719 42 705 L42 628 Q42 614 56 614 L108 614 L108 607 Z"/>
    <line class="fold-line-light" x1="108" y1="614" x2="108" y2="719"/>
    <line class="fold-line-light" x1="180" y1="607" x2="180" y2="719"/>
    <text class="brand-name" transform="translate(131,663) rotate(90)" font-size="13" text-anchor="middle">Swift Heron</text>
    <rect class="panel-dark" x="180" y="607" width="315" height="112"/>
    <circle cx="337" cy="647" r="9" fill="#ffffff"/>
    <text class="brand-name" x="337" y="697" font-size="34" text-anchor="middle">Swift Heron</text>
    <rect class="panel-light" x="495" y="607" width="527" height="112"/>
    <text class="product-name" x="540" y="677">BAMBOO TOOTHBRUSH</text>
    <rect x="900" y="609" width="96" height="108" fill="url(#bamboo-tone)" role="img" aria-label="Bamboo stalks with leaves illustration"/>

    <!-- Row 3: second side panel -->
    <rect class="panel-dark" x="135" y="719" width="360" height="74"/>
    <line class="fold-line-light" x1="180" y1="719" x2="180" y2="793"/>
    <rect class="panel-light" x="495" y="719" width="527" height="74"/>
    <path class="panel-light" d="M1022 721 L1067 721 L1067 769 L1060 791 L1022 791 Z"/>
    <g transform="translate(0,185)">
      <use href="#badge-row"/>
      <use href="#claim-row"/>
    </g>

    <!-- Row 4: back panel with right tuck flap -->
    <rect class="panel-dark" x="180" y="793" width="315" height="112"/>
    <circle cx="337" cy="833" r="9" fill="#ffffff"/>
    <text class="brand-name" x="337" y="883" font-size="34" text-anchor="middle">Swift Heron</text>
    <rect class="panel-light" x="495" y="793" width="527" height="112"/>
    <text class="product-name" x="540" y="862">BAMBOO TOOTHBRUSH</text>
    <rect x="900" y="795" width="96" height="108" fill="url(#bamboo-tone)" role="img" aria-label="Bamboo stalks with leaves illustration"/>
    <path class="panel-light" d="M1022 800 L1146 800 Q1160 800 1160 814 L1160 891 Q1160 905 1146 905 L1022 905 Z"/>
    <line class="fold-line" x1="1095" y1="800" x2="1095" y2="905"/>
    <text class="brand-name brand-name--flap" transform="translate(1044,848) rotate(90)" font-size="13" text-anchor="middle">Swift Heron</text>

    <!-- Row 5: glue flap -->
    <path class="panel-dark" d="M180 905 L495 905 L495 962 L196 962 Z"/>
    <path class="panel-light" d="M495 905 L1022 905 L1006 962 L495 962 Z"/>
  </g>
</svg>
</body>
</html>
```